Thistle Root Organic

Please find attached screenshots of a same product as what I'm selling, looking for similar packaging but yet a whole new different design with my own logo rivertiles which is also attached. It will be on white bags with the clear on the bottom center. As far as colors maby green yellow and black or if you have a better idea. Also it needs to be something that looks up to date modern I like when it has that two-tone gloss to it where it goes from darker to lighter.

```html
<!DOCTYPE html>
<html lang="en">
<head>
<meta charset="utf-8">
<title>Thistle Root Organic – Pouch Front</title>
<link href="https://fonts.googleapis.com/css2?family=Amatic+SC:wght@700&family=Fredoka:wght@600&family=Montserrat:wght@500&display=swap" rel="stylesheet">
<style>
  :root {
    --bg: #ffffff;
    --pouch-edge: #e4e7e5;
    --green-dark: #1d5436;
    --green-mid: #2e9460;
    --green-light: #8fd3ae;
    --herb-dark: #4b5a2c;
    --herb-light: #a9a86c;
  }
  html, body {
    margin: 0;
    width: 1200px;
    height: 1200px;
    overflow: hidden;
    background: var(--bg);
  }
  .canvas { position: relative; width: 1200px; height: 1200px; }
  .pouch {
    position: absolute;
    left: 323px; top: 142px;
    width: 559px; height: 908px;
    border-radius: 8px 8px 4px 4px;
    background: linear-gradient(100deg, #eceeed 0%, #ffffff 22%, #ffffff 70%, #f0f2f1 92%, #e6e9e7 100%);
    box-shadow: inset 0 0 0 1px var(--pouch-edge);
    overflow: hidden;
  }
  .seal-line { position: absolute; left: 10px; right: 10px; height: 2px; background: #e6e9e7; }
  .brand-frame {
    position: absolute;
    left: 467px; top: 123px;
    width: 251px; height: 277px;
    border: 10px solid transparent;
    border-top: none;
    border-image: linear-gradient(180deg, var(--green-dark) 0%, var(--green-mid) 55%, var(--green-light) 100%) 1;
  }
  .brand-mark {
    position: absolute;
    left: 50%; top: 124px;
    width: 76px; height: 76px;
    margin-left: -38px;
    border-radius: 50%;
    background: var(--green-mid);
  }
  .brand-name {
    position: absolute;
    left: 0; right: 0; top: 220px;
    text-align: center;
    font-family: "Montserrat", sans-serif;
    font-weight: 500;
    font-size: 30px;
    letter-spacing: 4px;
    color: var(--green-mid);
  }
  .title-art { position: absolute; left: 0; top: 0; }
  .plant-art {
    position: absolute;
    left: 717px; top: 651px;
    width: 109px; height: 150px;
    border-radius: 6px;
    background: linear-gradient(180deg, rgba(46,148,96,0.22), rgba(46,148,96,0.1));
  }
  .latin-name, .net-weight {
    position: absolute;
    left: 0; width: 1200px;
    text-align: center;
    font-family: "Amatic SC", sans-serif;
    font-weight: 700;
    color: var(--green-dark);
    margin: 0;
    line-height: 1;
  }
  .latin-name { top: 814px; font-size: 50px; }
  .net-weight { top: 874px; font-size: 38px; }
  .window {
    position: absolute;
    left: 396px; top: 940px;
    width: 414px; height: 110px;
    border-radius: 50% 50% 0 0 / 100% 100% 0 0;
    background: radial-gradient(ellipse at 50% 70%, var(--herb-light) 0%, #7d8249 45%, var(--herb-dark) 100%);
  }
</style>
</head>
<body>
<div class="canvas">
  <div class="pouch">
    <div class="seal-line" style="top:1px"></div>
    <div class="seal-line" style="top:19px"></div>
    <div class="seal-line" style="top:78px"></div>
    <div class="seal-line" style="top:97px"></div>
    <div class="seal-line" style="top:125px"></div>
  </div>

  <div class="brand-frame">
    <div class="brand-mark"></div>
    <div class="brand-name">RIVERTILES</div>
  </div>

  <svg class="title-art" width="1200" height="1200" viewBox="0 0 1200 1200" aria-label="Organic Thistle Root">
    <defs>
      <linearGradient id="titleFill" x1="0" y1="0" x2="0" y2="1">
        <stop offset="0" stop-color="#2b7a50"/>
        <stop offset="1" stop-color="#17452c"/>
      </linearGradient>
      <path id="titleArc" d="M408 660 Q612 590 818 660"/>
    </defs>
    <path d="M430 567 Q480 548 540 545" fill="none" stroke="var(--green-mid)" stroke-width="2"/>
    <path d="M688 545 Q760 548 822 575" fill="none" stroke="var(--green-mid)" stroke-width="2"/>
    <text x="613" y="549" text-anchor="middle" font-family="Amatic SC, sans-serif" font-weight="700" font-size="52" fill="var(--green-mid)">ORGANIC</text>
    <text font-family="Fredoka, sans-serif" font-weight="600" font-size="84" fill="url(#titleFill)">
      <textPath href="#titleArc" startOffset="50%" text-anchor="middle" textLength="400" lengthAdjust="spacing">THISTLE</textPath>
    </text>
    <text x="600" y="713" text-anchor="middle" font-family="Fredoka, sans-serif" font-weight="600" font-size="84" letter-spacing="6" fill="url(#titleFill)">ROOT</text>
    <path d="M417 762 Q560 718 730 724" fill="none" stroke="var(--green-mid)" stroke-width="2.5"/>
  </svg>

  <div class="plant-art" role="img" aria-label="Botanical line drawing of the flowering thistle plant"></div>

  <p class="latin-name">CIRSIUM VULGARE</p>
  <p class="net-weight">NET WT. 1.27 OZ. (36G)</p>

  <div class="window" role="img" aria-label="Clear window showing the dried cut root inside"></div>
</div>
</body>
</html>
```